Vorel constructions

We are predominantly a residential home builder based in Melbourne, Victoria Australia. We construct houses, apartments, townhouses, multi-unit developments.

The name of the company is "Vorel Constructions"
My company believes in building unique construction projects mainly residential homes. The target customers are upmarket Melbourne residents/investors.

I want the brand name "Vorel" to be part of the logo. There's no need to put the word construction in the logo at this stage.

I would also like some ideas for a slogan e.g. "Just build it." or "We build quality homes." But I would like something unique and different for a slogan not the same old cliche.

vorelconstructions.example.com.au
e: tmelo@vorelconstructions.example.com.au
M: 0417305862
Address: 8/3 Fenwick Lane Clayton VIC 3168

Director:Mr Dinesh Malarkodiyan

```html
<!DOCTYPE html>
<html lang="en">
<head>
<meta charset="utf-8">
<title>Vorel Constructions – Business Card</title>
<link rel="stylesheet" href="https://fonts.googleapis.com/css2?family=Open+Sans:wght@400;600;700&display=swap">
<style>
  :root {
    --stage: #2b2b2e;
    --card-deep: #140f26;
    --card-mid: #2c2546;
    --card-glow: #3a3158;
    --brand-cyan: #1eb3ea;
    --ink-light: #ffffff;
    --foot-band: #f4f4f6;
    --skyline: rgba(70, 58, 110, 0.28);
  }
  * { margin: 0; padding: 0; box-sizing: border-box; }
  html, body {
    width: 1200px; height: 800px; overflow: hidden;
    background: var(--stage);
    font-family: "Open Sans", Arial, sans-serif;
  }
  .stage {
    width: 1200px; height: 800px;
    display: flex; align-items: center; justify-content: center; gap: 40px;
  }
  .card {
    position: relative;
    width: 540px; height: 315px;
    overflow: hidden;
    box-shadow: 0 10px 30px rgba(0,0,0,0.45);
  }
  .card-front {
    background: radial-gradient(ellipse at 50% 40%, var(--card-glow) 0%, var(--card-mid) 40%, var(--card-deep) 100%);
    border-bottom: 10px solid var(--foot-band);
  }
  .card-back {
    background: radial-gradient(ellipse at 55% 40%, #221b3a 0%, var(--card-deep) 70%);
  }
  .skyline {
    position: absolute; left: 0; bottom: 0;
    width: 200px; height: 190px;
    background: linear-gradient(to top, var(--skyline), rgba(70,58,110,0));
  }
  .card-back .skyline { left: 30px; width: 220px; height: 200px; }
  .holder {
    position: absolute; top: 12px; left: 20px;
    color: var(--ink-light);
  }
  .holder-name { font-size: 13px; font-weight: 400; }
  .holder-role { font-size: 15px; font-weight: 400; margin-top: 2px; }
  .brand {
    position: absolute; top: 92px; left: 0; right: 0;
    display: flex; flex-direction: column; align-items: center;
  }
  .brand-row { display: flex; align-items: center; gap: 12px; }
  .brand-mark {
    width: 18px; height: 18px; border-radius: 50%;
    background: var(--brand-cyan);
  }
  .brand-name {
    font-size: 62px; font-weight: 600; line-height: 1;
    color: var(--brand-cyan); letter-spacing: 1px;
  }
  .brand-tagline {
    align-self: flex-end; margin-right: 178px; margin-top: 4px;
    font-size: 12px; color: var(--ink-light);
  }
  .contact {
    position: absolute; left: 0; right: 0; bottom: 14px;
    text-align: center; color: var(--ink-light);
    font-size: 11.5px; line-height: 1.45;
  }
  .contact b { font-weight: 700; }
  .back-brand {
    position: absolute; top: 105px; left: 0; right: 0;
    display: flex; justify-content: center; align-items: center; gap: 12px;
  }
  .back-brand .brand-name { font-size: 58px; }
</style>
</head>
<body>
<main class="stage">
  <section class="card card-front">
    <div class="skyline" role="img" aria-label="Faint skyline of tall buildings"></div>
    <div class="holder">
      <p class="holder-name">Mr. Dinesh Malarkodiyan</p>
      <p class="holder-role">Director</p>
    </div>
    <div class="brand">
      <div class="brand-row">
        <span class="brand-mark"></span>
        <span class="brand-name">Vorel</span>
      </div>
      <span class="brand-tagline">Rising Ground</span>
    </div>
    <div class="contact">
      <p><b>Address :</b> 8/3 Fenwick Lane Marrowdale VIC 3921</p>
      <p><b>Mail us :</b> tmelo@vorelconstructions.example.com.au | <b>Contact us :</b> 0417305862</p>
      <p><b>Visit us :</b> www.vorelconstructions.example.com.au</p>
    </div>
  </section>

  <section class="card card-back">
    <div class="skyline" role="img" aria-label="Faint skyline of tall buildings"></div>
    <div class="back-brand">
      <span class="brand-mark"></span>
      <span class="brand-name">Vorel</span>
    </div>
  </section>
</main>
</body>
</html>
```